Sunporch Tidy Works half fold brochure design

I need a brochure for a new company. The name of the company is Sunporch Tidy Works. I am a Professional Organizer. I am requesting a one fold brochure 11" wide x 8.5" high (obviously once folded 5.5" wide x 8.5" high) brochure. I have been told this may need to be designed as a flyer? I have attached a VERY BASIC layout of what I think I am looking for. I have also attached the original logos in all the different formats I have. I would like to have a very light green background & the text I have in orange please make orange. PLEASE feel free to add color to my "Sunporch Tidy Works" logo's and use light/soft green & orange shades if possible (OK to go darker for BOLD purposes) The brochure DOES NOT have to stick to this layout, again just what I THINK I want :) - THANK YOU

EDIT: 01-21-15 Remove MARGARET BELDANE from all 3 places (front, bottom inside right & back) Remove just the BELDANE from the 1st line on the back. PRIVACY & ETHICS on the back, please remove "PRIVACY &", leave Ethics and the 1st line of the text under it. Please remove all of the text following the 1st sentence. THANK YOU

```html
<!DOCTYPE html>
<html lang="en">
<head>
<meta charset="utf-8">
<title>Sunporch Tidy Works – Inside Spread</title>
<link href="https://fonts.googleapis.com/css2?family=Open+Sans:ital,wght@0,300;0,400;0,600;0,700;1,400&family=Roboto+Condensed:wght@400;700&display=swap" rel="stylesheet">
<style>
  :root {
    --orange: #f07a1e;
    --green: #57b947;
    --green-text: #3aa53a;
    --ink: #2a2a2a;
    --paper: #ffffff;
    --stage: #ecece8;
  }
  * { box-sizing: border-box; margin: 0; padding: 0; }
  html, body { width: 1200px; height: 1002px; overflow: hidden; background: var(--stage); }
  body { font-family: "Open Sans", Arial, sans-serif; color: var(--ink); }

  .spread {
    position: absolute; left: 30px; top: 60px; width: 1140px; height: 881px;
    display: flex; box-shadow: 0 6px 24px rgba(0,0,0,.18);
  }
  .page { position: relative; width: 570px; height: 881px; background: var(--paper); overflow: hidden; }
  .page--left { border-right: 1px solid #e2e2e2; }

  /* left page */
  .hero-photo { position: absolute; left: 0; top: 0; width: 570px; height: 360px; }
  .hero-quote {
    position: absolute; left: 300px; top: 150px; width: 240px;
    font-weight: 300; font-size: 17px; line-height: 1.3; color: #333; text-align: right;
  }
  .hero-quote .mark { color: var(--green); font-weight: 700; font-size: 26px; line-height: 0; }

  .faq-rail { position: absolute; left: 0; top: 350px; width: 140px; height: 531px; background: var(--green); }
  .faq-label {
    position: absolute; right: 22px; text-align: right;
    font-family: "Roboto Condensed", "Arial Narrow", sans-serif; font-size: 22px; line-height: 1.1; color: #fff;
  }
  .faq-notch { position: absolute; right: -1px; width: 0; height: 0;
    border-top: 14px solid transparent; border-bottom: 14px solid transparent; border-right: 14px solid var(--paper); }

  .faq-answer { position: absolute; left: 165px; width: 380px; font-size: 13.5px; line-height: 1.4; }
  .faq-answer h3 { color: var(--orange); font-size: 17px; font-weight: 700; margin-bottom: 2px; }

  .promise {
    position: absolute; left: 70px; top: 770px; width: 470px; padding: 16px 22px;
    background: var(--orange); color: #fff; border-radius: 14px;
    font-size: 13.5px; line-height: 1.4; box-shadow: 0 4px 8px rgba(0,0,0,.2);
  }

  /* right page */
  .page-rules { position: absolute; left: 0; top: 0; }
  .intro-col { position: absolute; top: 70px; width: 245px; font-size: 13px; line-height: 1.4; }
  .intro-col h2 { font-size: 17px; font-weight: 700; line-height: 1.2; margin-bottom: 10px; }
  .intro-col--anxiety { left: 25px; }
  .intro-col--anxiety h2 { color: var(--orange); }
  .intro-col--anxiety p { font-style: italic; }
  .intro-col--organizer { left: 300px; }
  .intro-col--organizer h2 { color: var(--green-text); }
  .intro-col .source { font-weight: 700; }

  .service-col { position: absolute; width: 250px; }
  .service-col--left { left: 30px; top: 405px; }
  .service-col--right { left: 300px; top: 385px; }
  .service { margin-bottom: 18px; }
  .service h4 { color: var(--orange); font-size: 13px; font-weight: 400; text-transform: uppercase; }
  .service li { list-style: none; color: var(--green-text); font-size: 14px; line-height: 1.3; }
  .service li::before { content: "• "; }
  .service-note { font-size: 12.5px; color: var(--ink); line-height: 1.35; }

  .team-photo {
    position: absolute; left: 80px; top: 645px; width: 450px; height: 225px;
    background: radial-gradient(ellipse at 50% 60%, #6b6e74 0%, #9ea3aa 55%, #ffffff 80%);
  }
  .brand-card {
    position: absolute; left: 180px; top: 760px; width: 250px; height: 78px;
    background: #f4f4f2; border: 1px solid #ccc; display: flex; align-items: center; justify-content: center;
    gap: 10px; box-shadow: 0 2px 6px rgba(0,0,0,.25);
  }
  .brand-card .dot { width: 14px; height: 14px; border-radius: 50%; background: var(--orange); flex: none; }
  .brand-card .name { font-size: 18px; font-weight: 600; color: var(--ink); white-space: nowrap; }
</style>
</head>
<body>
<main class="spread">
  <section class="page page--left">
    <svg class="hero-photo" viewBox="0 0 570 360" role="img" aria-label="Photo of smiling business people seated at a seminar, listening">
      <defs>
        <linearGradient id="heroTone" x1="0" y1="0" x2="1" y2="0">
          <stop offset="0" stop-color="#8d8a88"/>
          <stop offset=".45" stop-color="#d9cfc4"/>
          <stop offset="1" stop-color="#f4f2ef"/>
        </linearGradient>
      </defs>
      <path d="M0 70 Q280 10 570 40 L570 330 Q300 310 0 360 Z" fill="url(#heroTone)"/>
      <path d="M0 70 Q280 10 570 40" fill="none" stroke="var(--orange)" stroke-width="6"/>
      <path d="M0 358 Q300 310 570 330" fill="none" stroke="var(--orange)" stroke-width="6"/>
    </svg>
    <p class="hero-quote"><span class="mark">“</span> Getting organized isn’t all about everything being in its proper place. It can also require overcoming fears and anxieties. <span class="mark">”</span></p>

    <div class="faq-rail">
      <div class="faq-notch" style="top:22px"></div>
      <div class="faq-label" style="top:20px">How<br>Do I<br>Start?</div>
      <div class="faq-notch" style="top:170px"></div>
      <div class="faq-label" style="top:160px">Can I<br>Keep My<br>Things?</div>
      <div class="faq-notch" style="top:310px"></div>
      <div class="faq-label" style="top:300px">I Don’t<br>Have<br>the Time!</div>
    </div>

    <div class="faq-answer" style="top:365px">
      <h3>By getting help from a professional!</h3>
      <p>No one can do everything; everyone needs a helping hand at times. (I bring my vehicle to a mechanic when it needs service, even for just a simple oil change!)</p>
    </div>
    <div class="faq-answer" style="top:505px">
      <h3>Certainly you can!</h3>
      <p>There is a process that will help you decide what to keep and what you better part with. (I can help you determine the practical and monetary “worth” of something. Only you can determine its personal “value”.)</p>
    </div>
    <div class="faq-answer" style="top:645px">
      <h3>Now you will!</h3>
      <p>Getting organized will actually save you time. You will know where that “thing” is, find it quickly and avoid the time it takes to run out and purchase a new “thing”. (You will have actually created more time to enjoy the lifestyle that is important to you.)</p>
    </div>

    <p class="promise">Whether you are too busy, too confused, over whelmed, tired, stressed or just don’t know where to start, I offer a variety of hands on services to help you bring a sense of fun, freedom and functionality to almost any space.</p>
  </section>

  <section class="page page--right">
    <svg class="page-rules" width="570" height="400" viewBox="0 0 570 400" aria-hidden="true">
      <path d="M0 40 Q280 10 570 20" fill="none" stroke="var(--orange)" stroke-width="6"/>
      <path d="M0 385 Q290 345 570 350" fill="none" stroke="var(--orange)" stroke-width="4"/>
    </svg>

    <article class="intro-col intro-col--anxiety">
      <h2>Why Dealing with Anxieties is Important?</h2>
      <p>We all have anxiety about something that prevents or inhibits us from taking action toward a solution. Whether you want someone to take over the project or a helping hand (nudge) is all you really need, a professional organizer is the perfect way to get started. Getting organized is going to be a process of progress, not perfection. It will require some level of support and continued work on you part, but the rewards will far outweigh the efforts.</p>
    </article>
    <article class="intro-col intro-col--organizer">
      <h2>What is a Professional Organizer?</h2>
      <p>“A Professional Organizer enhances the lives of clients by designing systems and processes using organizing principles and through transferring organizing skills. Professional Organizers help individuals and businesses take control of their surroundings, their time, their paper, and their systems for life.” <span class="source">– Guild of Home Organizing Professionals.</span></p>
    </article>

    <div class="service-col service-col--left">
      <div class="service"><h4>Attic – to – Basement:</h4><ul><li>Sorting – Purging – Organizing</li></ul></div>
      <div class="service"><h4>Paper Control:</h4><ul><li>Sorting – Purging - Organizing</li><li>Household, home office &amp; home based filing systems</li></ul></div>
      <div class="service"><h4>Downsizing:</h4><ul><li>Sorting – purging - organizing - labeling</li><li>Packing &amp; unpacking</li></ul></div>
    </div>
    <div class="service-col service-col--right">
      <div class="service"><h4>Removal:</h4><ul><li>Light trash &amp; proper disposal</li><li>Donations &amp; light recyclables to proper locations</li><li>Shredding Service</li></ul></div>
      <div class="service"><h4>Follow Up:</h4><ul><li>Routine “clutter maintenance” visits</li></ul></div>
      <p class="service-note">*For projects not listed above, please contact me</p>
    </div>

    <div class="team-photo" role="img" aria-label="Photo of a large group of business people standing together"></div>
    <div class="brand-card"><span class="dot"></span><span class="name">Sunporch Tidy Works</span></div>
  </section>
</main>
</body>
</html>
```